Business letterhead and powerpoint template

Hi, I have recently started using a new logo (found through PixelGrove) and would now like to use that logo for letterheads and powerpoint.

Attached is the logo and one version of a brochure I have recently used.

Industry/Entity Type

Business

```html
<!DOCTYPE html>
<html lang="en">
<head>
<meta charset="utf-8">
<title>Kestrel Capital – Stationery Set</title>
<link href="https://fonts.googleapis.com/css2?family=Questrial&family=Arimo:wght@400&family=Tinos&display=swap" rel="stylesheet">
<style>
  :root {
    --brand-orange: #ee4d23;
    --ink: #3a3a3c;
    --ink-soft: #6d6e70;
    --paper: #ffffff;
    --faint: #e6e7e8;
    --flap: #b4b5b7;
    --window: #d1d2d4;
    --outline: #8a8a8a;
  }
  * { box-sizing: border-box; margin: 0; padding: 0; }
  html, body { width: 1200px; height: 779px; overflow: hidden; background: var(--paper); }
  .canvas { position: relative; width: 1200px; height: 779px; font-family: "Questrial", sans-serif; color: var(--ink); }

  .sheet { position: absolute; background: var(--paper); border: 1px solid var(--outline); box-shadow: 4px 5px 6px rgba(0,0,0,.18); overflow: hidden; }

  .wordmark { display: flex; align-items: center; gap: 7px; font-family: "Questrial", sans-serif; font-size: 15px; letter-spacing: 1px; color: var(--ink); white-space: nowrap; }
  .wordmark .mark-square { width: 12px; height: 12px; background: var(--brand-orange); }
  .wordmark--light { color: var(--paper); }

  .faint-motif { position: absolute; border-radius: 50%; background: var(--faint); }

  .address { font-size: 10px; line-height: 12.5px; color: var(--ink-soft); }

  /* business card – front */
  .card-front { left: 43px; top: 68px; width: 265px; height: 170px; }
  .card-front .faint-motif { left: 185px; top: 30px; width: 140px; height: 140px; }
  .card-front .wordmark { position: absolute; left: 20px; top: 36px; }
  .card-front .company { position: absolute; left: 20px; top: 88px; font-size: 12px; letter-spacing: 1.2px; color: var(--ink); }
  .card-front .address { position: absolute; left: 20px; top: 116px; font-size: 9.5px; line-height: 12px; }

  /* business card – back */
  .card-back { left: 366px; top: 72px; width: 265px; height: 167px; background: var(--brand-orange); border-color: var(--brand-orange); }
  .card-back .wordmark { position: absolute; left: 0; right: 0; top: 58px; justify-content: center; }
  .card-back .contact { position: absolute; left: 74px; top: 112px; font-size: 10px; line-height: 12px; color: var(--paper); letter-spacing: .3px; }

  /* envelope */
  .envelope { position: absolute; left: 33px; top: 300px; width: 567px; height: 318px; }
  .envelope-flap { position: absolute; left: 0; top: 0; width: 567px; height: 36px; }
  .envelope-body { left: 0; top: 35px; width: 567px; height: 283px; }
  .envelope-body .faint-motif { left: 390px; top: 40px; width: 230px; height: 230px; }
  .envelope-body .wordmark { position: absolute; left: 26px; top: 42px; }
  .envelope-body .address { position: absolute; left: 26px; top: 82px; }
  .address-window { position: absolute; left: 27px; top: 186px; width: 160px; height: 50px; border-radius: 6px; background: var(--window); border: 1px solid #a7a9ac; }

  /* letterhead */
  .letterhead { left: 684px; top: 36px; width: 475px; height: 671px; box-shadow: 5px 6px 8px rgba(0,0,0,.2); }
  .letterhead .wordmark { position: absolute; right: 44px; top: 38px; }
  .letterhead-rule { position: absolute; left: 80px; top: 75px; width: 350px; height: 2px; background: var(--brand-orange); }
  .letter-body { position: absolute; left: 89px; top: 157px; width: 320px; font-family: "Arimo", sans-serif; font-size: 8.6px; line-height: 12.2px; color: #2d2d2d; }
  .letter-body p { margin-bottom: 12px; }
  .letter-body .recipient { margin-bottom: 36px; }
  .letter-body .date { margin-bottom: 46px; }
  .letter-body .salutation { margin-bottom: 8px; }
  .letter-close { position: absolute; left: 89px; top: 532px; font-family: "Tinos", serif; font-size: 8.6px; line-height: 10.5px; color: #2d2d2d; }
  .signature { width: 120px; height: 26px; margin: 4px 0 0; background: linear-gradient(90deg, #2d2d2d22, #2d2d2d55, #2d2d2d22); border-radius: 3px; }
  .signatory { margin-bottom: 20px; }
  .copies span { display: block; padding-left: 17px; }
  .copies span:first-child { padding-left: 0; }

  /* disc */
  .disc { position: absolute; left: 484px; top: 493px; width: 264px; height: 264px; }
</style>
</head>
<body>
<main class="canvas">

  <section class="sheet card-front" aria-label="Business card front">
    <div class="faint-motif"></div>
    <div class="wordmark"><span class="mark-square"></span>KESTREL CAPITAL</div>
    <div class="company">KESTREL CAPITAL</div>
    <div class="address">Level 8 Suite 14<br>48 Ridgeline Avenue<br>Northbay 2100 NSW<br>Australia</div>
  </section>

  <section class="sheet card-back" aria-label="Business card back">
    <div class="wordmark wordmark--light">KESTREL CAPITAL</div>
    <div class="contact">Phone: +61 (0)2 5550 1420<br>Fax: +61 (0)2 5550 1499<br>Phone: +61 (0)2 5550 1420<br>WWW.kestrelcapital.com.au</div>
  </section>

  <section class="envelope" aria-label="DL window envelope">
    <svg class="envelope-flap" viewBox="0 0 567 36" aria-hidden="true">
      <polygon points="0,36 40,0 527,0 567,36" fill="var(--flap)"/>
    </svg>
    <div class="sheet envelope-body">
      <div class="faint-motif"></div>
      <div class="wordmark"><span class="mark-square"></span>KESTREL CAPITAL</div>
      <div class="address">Level 8 Suite 14<br>48 Ridgeline Avenue<br>Northbay 2100 NSW<br>Australia</div>
      <div class="address-window"></div>
    </div>
  </section>

  <section class="sheet letterhead" aria-label="Letterhead">
    <div class="wordmark"><span class="mark-square"></span>KESTREL CAPITAL</div>
    <div class="letterhead-rule"></div>
    <div class="letter-body">
      <p class="recipient">Domnul Numele Destinatarului,<br>Adresa Destinatarului<br>Oras, Judet Cod postal</p>
      <p class="date">Iasi, Ziua Luna, Anul</p>
      <p class="salutation">Domnului Numele Destinatarului,</p>
      <p>Lorem ipsum dolor sit amet, consectetuer adipiscing elit, sed diam nonummy nibh euismod tincidunt ut laoreet dolore magna aliquam erat volutpat. Ut wisi enim ad minim veniam, quis nostrud exerci tation ullamcorper suscipit lobortis nisl ut aliquip ex ea commodo.</p>
      <p>Duis autem vel eum iriure dolor in hendrerit in vulputate velit esse molestie consequat, vel illum dolore eu feugiat nulla facilisis at vero eros et accumsan et iusto odio dignissim qui blandit praesent lup tatum zzril delenit augue duis scing elit, sed diam nonummy nibh euismod tincidunt ut laoreet dolore magna aliquam erat volutpat.</p>
      <p>Ut wisi enim ad minim veniam, quis nostrud exerci tation ullamcorper suscipit dolor in hendrerit in vulputate velit esse molestie consequat, vel illum dolore eu feugiat nulla facilisis at vero eros et accumsan et iusto odio dignissim qui blandit praesent luptatum zzril delenit augue duis dolore te feugait nulla facilisi. Ut laoreet dolore magna aliquam erat volutpat. Ut wisi enim ad minim veniam, quis nostrud exerci tation ullamcorper suscipit lobortis nisl ut aliquip ex ea commodo consequat.</p>
    </div>
    <div class="letter-close">
      <div>Sincerely,</div>
      <div class="signature" role="img" aria-label="Handwritten signature of Daniel Corwin"></div>
      <div class="signatory">Daniel Corwin<br>Deputy Assistant Director</div>
      <div class="copies"><span>Cc:&nbsp; L. Harding</span><span>T. Moreau</span></div>
    </div>
  </section>

  <svg class="disc" viewBox="0 0 264 264" aria-label="Branded disc label">
    <circle cx="132" cy="132" r="131" fill="var(--paper)" stroke="#222" stroke-width="1"/>
    <circle cx="132" cy="132" r="126" fill="var(--brand-orange)"/>
    <circle cx="132" cy="132" r="44" fill="var(--paper)" stroke="#999" stroke-width=".8"/>
    <circle cx="132" cy="132" r="36" fill="#eceded" stroke="#777" stroke-width=".8"/>
    <circle cx="132" cy="132" r="17" fill="var(--paper)" stroke="#888" stroke-width=".8"/>
    <rect x="24" y="123" width="34" height="16" rx="2" fill="var(--paper)"/>
    <text x="212" y="135" text-anchor="middle" font-family="Questrial, sans-serif" font-size="7.5" letter-spacing=".4" fill="var(--paper)">KESTREL CAPITAL</text>
  </svg>

</main>
</body>
</html>
```